Minimalist- A clean spacious and crisp design for a Security Consulting Company

I need a design for a security consultant that deals with the upper end of town for security design, including CCTV and other electronic design. I need it to look spacious and be very simplistic in design. I want to keep it looking like Vantro or QUIBA's website. I have experience in business intelligence. and have a lot of high end clients in the diamond industry and mining. My key area of income is consulting and taking them from normal to excellent security.
Target Market(s)
People interested in doing business with me
Industry/Entity Type
Electronic
Coding
Coded - Design and coding required
Number of Pages Required
4 page
Requirements
Must have
- The least amount of text possible
- A simple and nice front page with the logo.
- A contact us button
- Specialised projects button
- About us button
- Business intelligence button
Should not have
- Cluttered un-useful information

```html
<!DOCTYPE html>
<html lang="en">
<head>
<meta charset="utf-8">
<title>Halden Strategy</title>
<link href="https://fonts.googleapis.com/css2?family=Cinzel:wght@400;600&family=Raleway:wght@300;400&display=swap" rel="stylesheet">
<style>
  :root {
    --red: #c0272d;
    --ink: #1b1b1b;
    --dark-panel: #2e2f31;
    --panel-text: #e6e6e6;
    --icon-dark: #3a3f47;
    --white: #ffffff;
  }
  * { margin: 0; padding: 0; box-sizing: border-box; }
  html, body { width: 1200px; height: 1170px; overflow: hidden; background: var(--white); }
  body { position: relative; font-family: "Raleway", sans-serif; color: var(--ink); }

  .site-header { position: absolute; left: 0; top: 0; width: 1200px; height: 113px; }
  .brand { position: absolute; left: 178px; top: 44px; display: flex; align-items: center; gap: 8px; }
  .brand-mark { width: 34px; height: 34px; background: var(--red); }
  .brand-name { font-family: "Cinzel", serif; font-weight: 600; font-size: 23px; color: var(--ink); letter-spacing: 0.2px; }

  .main-nav { position: absolute; top: 55px; right: 172px; display: flex; align-items: center; gap: 2px; }
  .main-nav a { font-family: "Cinzel", serif; font-size: 13px; text-transform: uppercase; color: var(--ink); text-decoration: none; padding: 6px 9px; line-height: 15px; white-space: nowrap; }
  .main-nav a.is-active { background: var(--red); color: var(--white); }

  .hero { position: absolute; left: 0; top: 113px; width: 1200px; height: 562px;
    background: linear-gradient(100deg, #d9dadb 0%, #eef0f1 30%, #c9ced3 55%, #e7e8e9 75%, #4a4c50 100%); }

  .hero-caption { position: absolute; left: 176px; top: 588px; width: 846px; height: 106px; background: var(--white); padding: 7px 6px 0 7px; }
  .hero-caption-inner { background: var(--dark-panel); height: 99px; text-align: center; padding-top: 20px; }
  .hero-title { font-family: "Cinzel", serif; font-weight: 400; font-size: 31px; color: var(--white); letter-spacing: 1px; line-height: 34px; }
  .hero-subtitle { font-family: "Raleway", sans-serif; font-weight: 300; font-size: 21px; color: var(--panel-text); margin-top: 2px; }

  .plan-item { position: absolute; left: 219px; width: 780px; }
  .plan-icon { position: absolute; left: 0; top: 0; width: 52px; height: 56px; }
  .plan-heading { position: absolute; left: 80px; top: 0; font-family: "Cinzel", serif; font-weight: 400; font-size: 30px; text-transform: uppercase; color: var(--red); line-height: 32px; }
  .plan-text { position: absolute; left: 80px; font-size: 12.5px; line-height: 14.5px; width: 700px; }

  .plan-vision { top: 736px; }
  .plan-vision .plan-text { top: 38px; }
  .plan-mission { top: 849px; }
  .plan-mission .plan-text { top: 38px; width: 650px; }
  .plan-values { top: 969px; }
  .plan-values .plan-text { top: 38px; font-size: 11px; line-height: 13.5px; width: 660px; }

  .site-footer { position: absolute; left: 0; top: 1128px; width: 1200px; height: 42px; background: var(--red); color: var(--white); font-size: 11.5px; text-align: center; line-height: 42px; }
</style>
</head>
<body>
  <header class="site-header">
    <div class="brand">
      <span class="brand-mark"></span>
      <span class="brand-name">Halden Strategy</span>
    </div>
    <nav class="main-nav">
      <a class="is-active" href="#">Home</a>
      <a href="#">About Us</a>
      <a href="#">Specialised Projects</a>
      <a href="#">Business Intelligence</a>
      <a href="#">Contact Us</a>
    </nav>
  </header>

  <div class="hero" role="img" aria-label="Photo of a consultant at a desk watching several monitors showing CCTV camera feeds of corridors and warehouses"></div>

  <section class="hero-caption">
    <div class="hero-caption-inner">
      <h1 class="hero-title">Strategic &amp; Operational Plan</h1>
      <p class="hero-subtitle">Our People and Our Proccesses are the difference!</p>
    </div>
  </section>

  <section class="plan-item plan-vision">
    <svg class="plan-icon" viewBox="0 0 52 56">
      <g stroke="var(--red)" stroke-width="3" stroke-linecap="round">
        <line x1="26" y1="2" x2="26" y2="7"/><line x1="13" y1="7" x2="16" y2="11"/><line x1="39" y1="7" x2="36" y2="11"/>
        <line x1="4" y1="18" x2="9" y2="19"/><line x1="48" y1="18" x2="43" y2="19"/>
        <line x1="5" y1="32" x2="10" y2="30"/><line x1="47" y1="32" x2="42" y2="30"/>
      </g>
      <path d="M26 13a12 12 0 0 0-7 21.5V40h14v-5.5A12 12 0 0 0 26 13z" fill="none" stroke="var(--icon-dark)" stroke-width="3"/>
      <rect x="19" y="43" width="14" height="3" fill="var(--icon-dark)"/>
      <rect x="21" y="48" width="10" height="4" rx="1" fill="var(--icon-dark)"/>
    </svg>
    <h2 class="plan-heading">Vission</h2>
    <p class="plan-text">We a united Halden Strategy Team are committed to growing our people and refining our processes to produce a minimum of 10% increase in our profit perquarter in 2014 n addition we are focussed on building our Client base &nbsp;by one new Client per quarter, in 2014.</p>
  </section>

  <section class="plan-item plan-mission">
    <svg class="plan-icon" viewBox="0 0 52 56">
      <rect x="4" y="30" width="8" height="16" fill="var(--red)"/>
      <rect x="16" y="20" width="8" height="26" fill="var(--red)"/>
      <path d="M1 31l7-8 7 8z" fill="var(--red)"/>
      <path d="M13 21l7-9 7 9z" fill="var(--red)"/>
      <rect x="30" y="14" width="10" height="32" fill="var(--icon-dark)"/>
      <circle cx="35" cy="8" r="5" fill="var(--icon-dark)"/>
      <rect x="1" y="49" width="50" height="4" fill="var(--icon-dark)"/>
    </svg>
    <h2 class="plan-heading">Mission</h2>
    <p class="plan-text">As a Team we are committed to building mutual respect between each member and our Clients. Based on mutual respect we will develop mutually rewardig relationships between our team members and our Clients.</p>
  </section>

  <section class="plan-item plan-values">
    <svg class="plan-icon" viewBox="0 0 52 56">
      <circle cx="20" cy="7" r="5" fill="var(--icon-dark)"/>
      <rect x="13" y="14" width="14" height="22" rx="3" fill="var(--icon-dark)"/>
      <rect x="15" y="34" width="4" height="18" fill="var(--icon-dark)"/>
      <rect x="21" y="34" width="4" height="18" fill="var(--icon-dark)"/>
      <circle cx="35" cy="40" r="13" fill="var(--white)" stroke="var(--red)" stroke-width="3.5"/>
      <path d="M35 32v8l5 4" fill="none" stroke="var(--red)" stroke-width="2.5" stroke-linecap="round"/>
    </svg>
    <h2 class="plan-heading">Values</h2>
    <p class="plan-text">We a united Halden Strategy Team are committed to growing our people and refining our processes to produce a minimum of 10% increase in our profit perquarter in 2014 n addition we are focussed on building our Client base &nbsp;by one new Client per quarter, in 2014.</p>
  </section>

  <footer class="site-footer">© Copyright 2015, Halden Strategy, Inc. All rights reserved.</footer>
</body>
</html>
```